Business Card Redesign

We are looking for a designer to redesign our current business card (attached below). The logo itself will not change but the look and feel of the rest of the card needs to be freshened up. The text on the back of the card is to be changed to:
Strategic Alignment
Leadership and Coaching
Sales Force Development
Sales Talent Acquisition
Emotional Intelligence Facilitation & Certification
Guest speaking

The byline needs to be retained "Honest Connections... Confident living" along with the logo.

All up we will need business cards laid out for 6 people.

Also, once we receive a design that we are happy with we will need the branding to be continued through onto other documentation such as workbook cover pages, email signatures etc and will negotiate with the successful designer on this future piece of work.

Please review our website for more of an idea of who we are, our style, and what we do. www.brightoakpartners.com.au and www.heartwisecapability-hw-c.com.au.

Thank you for your interest.

```html
<!DOCTYPE html>
<html lang="en">
<head>
<meta charset="utf-8">
<title>Bright Oak Partners – Business Card, Option 1</title>
<link rel="stylesheet" href="https://fonts.googleapis.com/css2?family=Jost:wght@300;400;500&display=swap">
<style>
  :root {
    --blue-deep: #0a12e6;
    --blue-bright: #1e90ff;
    --grey-text: #5a5a5a;
    --label: #111111;
    --card-border: #333333;
    --paper: #ffffff;
  }
  * { margin: 0; padding: 0; box-sizing: border-box; }
  html, body {
    width: 938px; height: 1200px; overflow: hidden;
    background: var(--paper);
    font-family: "Jost", "Futura", sans-serif;
  }
  .sheet { position: relative; width: 938px; height: 1200px; }

  .option-label {
    position: absolute; top: 0; left: 0; width: 100%;
    text-align: center; font-weight: 300; font-size: 28px;
    color: var(--label); line-height: 34px;
  }

  .card {
    position: absolute; left: 0; width: 938px; height: 536px;
    border: 1px solid var(--card-border); background: var(--paper);
  }
  .card--front { top: 54px; }
  .card--back { top: 664px; }

  .contact {
    position: absolute; right: 53px; top: 50px;
    text-align: right; font-weight: 300; line-height: 1;
  }
  .contact__name { font-weight: 400; font-size: 37px; color: var(--blue-deep); letter-spacing: -0.5px; }
  .contact__title { margin-top: 9px; font-size: 26.5px; color: var(--blue-bright); }
  .contact__phone { margin-top: 24px; font-size: 26px; color: var(--blue-deep); }
  .contact__email { margin-top: 9px; font-size: 23px; color: var(--blue-bright); }
  .contact__web { margin-top: 7px; font-size: 23px; color: var(--blue-bright); }

  .brand {
    position: absolute; left: 52px; top: 380px;
    display: flex; align-items: center; gap: 14px;
  }
  .brand__dot { width: 30px; height: 30px; border-radius: 50%; background: var(--blue-deep); }
  .brand__name {
    font-weight: 500; font-size: 50px; line-height: 1;
    color: var(--blue-deep); letter-spacing: -1px;
  }
  .tagline {
    position: absolute; left: 85px; top: 476px;
    font-weight: 300; font-size: 24px; color: var(--grey-text);
  }

  .services {
    position: absolute; left: 53px; top: 72px;
    list-style: none; font-weight: 300; font-size: 30px; line-height: 52.6px;
  }
  .services li:nth-child(odd) { color: var(--blue-bright); }
  .services li:nth-child(even) { color: var(--blue-deep); }

  .address {
    position: absolute; left: 0; width: 100%; top: 478px;
    text-align: center; font-weight: 400; font-size: 30px; color: var(--blue-deep);
  }
</style>
</head>
<body>
<main class="sheet">
  <p class="option-label">Option 1</p>

  <section class="card card--front" aria-label="Card front">
    <div class="contact">
      <p class="contact__name">Mara Linden</p>
      <p class="contact__title">Client Services Manager</p>
      <p class="contact__phone">+ 613 9555 0142</p>
      <p class="contact__email">mara@brightoakpartners.com.au</p>
      <p class="contact__web">www.brightoakpartners.com.au</p>
    </div>

    <div class="brand">
      <span class="brand__dot" aria-hidden="true"></span>
      <span class="brand__name">Bright Oak Partners</span>
    </div>
    <p class="tagline">Honest Connections... Confident living</p>
  </section>

  <section class="card card--back" aria-label="Card back">
    <ul class="services">
      <li>Strategic Alignment</li>
      <li>Leadership and Coaching</li>
      <li>Sales Force Development</li>
      <li>Sales Talent Acquisition</li>
      <li>Emotional Intelligence Facilitation and Certification</li>
      <li>Guest speaking</li>
    </ul>
    <p class="address">Suite 4.08, 212 Kingsford Pde, Ashvale, Australia - 3190</p>
  </section>
</main>
</body>
</html>
```